New Massage Business needs a Card design

We need a card design for our new massage therapy business based in Sydney, Au. The business is getting a makeover, so a little later on we'll need shirts, various pamphlets and promotional flyers, and possibly a website. The winner will be offered those jobs as well.

Colour scheme should be green, black, and steel/charcoal grey. The business focuses on massage as an anatomical solution to stress, muscle aches, pains and fatigue. Ideally we'd like an anatomical image of the muscle system (ref to the attached files). In my mind this image takes up most of the left third of the card, and shows points of tension and pain at the neck and lower back. This image should be the grey portion of the card.

On the upper right is the other image attached, with a simple line drawing of a vehicle on the left end of the line, and a building on the right end replacing the stick figure (we have a therapist specializing in mobile massage). The blank part in the middle of the line should have "Kestrel Wellness", and in smaller writing below, "The Tension Fix".

Bottom right corner should have the contact and business details.
On the back we'd like a "next appointment" and "refer a friend" option.

If you have a design which doesn't fit the above, but you feel suits the business, please submit anyway - sometimes you don't know what you like until you see it.

Business Details:
Name: Kestrel Wellness - The Tension Fix

Industry/Entity Type

Massage Therapy

Contact Information for Business Card

Business Details:
Contact name: Marcus
Title: Massage Therapist
Contact: 0458203617
Email: info@ktfbodywork.example

Requirements
Must have
• Colour scheme should be green, black, and steel/charcoal grey. The business focuses on massage as an anatomical solution to stress, muscle aches, pains and fatigue. Ideally we'd like an anatomical image of the muscle system (ref to the attached files). In my mind this image takes up most of the left third of the card, and shows points of tension and pain at the neck and lower back. This image should be the grey portion of the card.
• On the upper right is the other image attached, with a simple line drawing of a vehicle on the left end of the line, and a building on the right end replacing the stick figure (we have a therapist specializing in mobile massage). The blank part in the middle of the line should have "Kestrel Wellness", and in smaller writing below, "The Tension Fix".
• Bottom right corner should have the contact and business details.
• On the back we'd like a "next appointment" and "refer a friend" option.
Nice to have
• Matt finish - no gloss
• If you have a design which doesn't fit the above, but you feel suits the business, please submit anyway - sometimes you don't know what you like until you see it.
Should not have
• Anything 'Zen'. The business promotes the physiological and scientific benefits of massage. For clients with spiritual or meditative needs, we refer out.

```html
<!DOCTYPE html>
<html lang="en">
<head>
<meta charset="utf-8">
<title>Kestrel Wellness – Business Card</title>
<link rel="stylesheet" href="https://fonts.googleapis.com/css2?family=Raleway:wght@400;500;700&display=swap">
<style>
  :root {
    --page-bg: #e9ebe6;
    --green-light: #d6e56e;
    --green-mid: #b4d153;
    --green-deep: #86ad36;
    --ink: #121212;
    --band: #141414;
    --white: #ffffff;
    --figure-light: #a8c65a;
    --figure-dark: #6f9433;
  }
  * { box-sizing: border-box; margin: 0; padding: 0; }
  html, body { width: 1200px; height: 1000px; overflow: hidden; }
  body {
    background: var(--page-bg);
    font-family: "Raleway", Arial, sans-serif;
    color: var(--ink);
    position: relative;
  }
  .card {
    position: absolute;
    left: 265px;
    width: 667px;
    height: 398px;
    border-radius: 22px;
    overflow: hidden;
    background: radial-gradient(ellipse 70% 75% at 62% 45%, var(--green-light) 0%, var(--green-mid) 55%, var(--green-deep) 100%);
    box-shadow: 0 6px 14px rgba(0,0,0,0.25);
  }
  .card--front { top: 73px; }
  .card--back { top: 532px; }

  .band { position: absolute; left: 0; width: 100%; display: block; }

  /* Front */
  .anatomy-figure {
    position: absolute;
    left: 32px; top: 0;
    width: 300px; height: 372px;
    border-radius: 120px 120px 10px 10px;
    background: linear-gradient(180deg, var(--figure-light) 0%, var(--figure-dark) 100%);
    opacity: 0.85;
  }
  .brand {
    position: absolute;
    right: 32px; top: 22px;
    width: 270px;
    text-align: center;
  }
  .brand__mark {
    display: block;
    width: 108px; height: 108px;
    margin: 0 auto 18px;
    border-radius: 50%;
    background: var(--ink);
  }
  .brand__name {
    font-size: 27px;
    font-weight: 500;
    letter-spacing: 0.5px;
    text-transform: uppercase;
    line-height: 1;
    color: var(--ink);
    white-space: nowrap;
  }
  .brand__tagline {
    margin-top: 6px;
    font-size: 13px;
    font-weight: 500;
    letter-spacing: 5px;
    text-transform: uppercase;
    color: var(--ink);
    white-space: nowrap;
  }
  .contact {
    position: absolute;
    right: 33px; top: 232px;
    text-align: right;
  }
  .contact__name { font-size: 21px; font-weight: 700; line-height: 1.2; }
  .contact__title { font-size: 17px; font-weight: 400; }
  .contact__line {
    display: flex; justify-content: flex-end; align-items: center; gap: 8px;
    font-size: 16px; margin-top: 6px;
  }
  .contact__phone { margin-top: 14px; }
  .icon { width: 15px; height: 12px; fill: none; stroke: var(--white); stroke-width: 1.4; }
  .icon--solid { fill: var(--white); stroke: none; }

  /* Back */
  .appointment__heading {
    position: absolute; top: 30px; width: 100%;
    text-align: center; font-size: 17px; font-weight: 700;
  }
  .days {
    position: absolute; top: 120px; left: 33px; right: 33px;
    display: flex; justify-content: space-between;
    list-style: none;
  }
  .day { display: flex; align-items: center; gap: 10px; font-size: 16px; font-weight: 700; }
  .day__box {
    width: 27px; height: 18px;
    border: 2px solid var(--ink);
    border-radius: 6px;
  }
  .date-line {
    position: absolute; left: 137px; top: 204px;
    width: 393px; height: 2px; background: var(--ink);
  }
  .date-label {
    position: absolute; top: 214px;
    font-size: 16px; font-weight: 500;
  }
  .date-label--date { left: 230px; }
  .date-label--time { left: 397px; }
  .referral {
    position: absolute; top: 268px; width: 100%;
    text-align: center; color: var(--white);
    font-size: 20px; font-weight: 400;
  }
  .policy {
    position: absolute; top: 325px; width: 100%;
    text-align: center;
  }
  .policy__heading { font-size: 16px; font-weight: 700; }
  .policy__text { font-size: 16px; margin-top: 6px; }
</style>
</head>
<body>

<section class="card card--front">
  <div class="anatomy-figure" role="img" aria-label="Anatomical illustration of the back muscles with tension points marked at the neck and lower back"></div>

  <div class="brand">
    <span class="brand__mark"></span>
    <div class="brand__name">Kestrel Wellness</div>
    <div class="brand__tagline">The Tension Fix</div>
  </div>

  <div class="contact">
    <div class="contact__name">Marcus Hartley</div>
    <div class="contact__title">Massage Therapist</div>
    <div class="contact__line contact__phone">0458203617
      <svg class="icon icon--solid" viewBox="0 0 15 12"><path d="M1 4 Q7.5 -1 14 4 L12 5.5 L10 4 L10 3 Q7.5 2 5 3 L5 4 L3 5.5 Z"/><rect x="3" y="6" width="9" height="5" rx="1"/></svg>
    </div>
    <div class="contact__line">info@ktfbodywork.example
      <svg class="icon" viewBox="0 0 15 12"><rect x="1" y="1.5" width="13" height="9" fill="#ffffff" stroke="none"/><path d="M1 1.5 L7.5 7 L14 1.5" stroke="#b4d153"/></svg>
    </div>
  </div>

  <svg class="band" style="top:340px;height:58px" viewBox="0 0 667 58" preserveAspectRatio="none" aria-hidden="true">
    <path d="M0 12 Q333 34 667 6 L667 58 L0 58 Z" fill="var(--band)"/>
  </svg>
</section>

<section class="card card--back">
  <h2 class="appointment__heading">YOUR NEXT APPOINTMENT IS:</h2>
  <ul class="days">
    <li class="day">Mon <span class="day__box"></span></li>
    <li class="day">Tue <span class="day__box"></span></li>
    <li class="day">Wed <span class="day__box"></span></li>
    <li class="day">Thur <span class="day__box"></span></li>
    <li class="day">Fri <span class="day__box"></span></li>
    <li class="day">Sat <span class="day__box"></span></li>
  </ul>
  <div class="date-line"></div>
  <span class="date-label date-label--date">DATE</span>
  <span class="date-label date-label--time">TIME</span>

  <svg class="band" style="top:248px;height:72px" viewBox="0 0 667 72" preserveAspectRatio="none" aria-hidden="true">
    <path d="M0 6 Q333 30 667 2 L667 72 Q333 46 0 70 Z" fill="var(--band)"/>
  </svg>
  <p class="referral">Refer to friends and get 30% OFF</p>

  <div class="policy">
    <h3 class="policy__heading">CANCELATION POLICY</h3>
    <p class="policy__text">If you are unable to keep your appointment , please allow 24 hours notice</p>
  </div>
</section>

</body>
</html>
```